Cobalt Bridge Capital - Letterhead

We need letterhead options for our case funding company called Cobalt Bridge Capital. Here are some of the details:

Name - Cobalt Bridge Capital
Phone - (555) 214 - 9087
Address - 58 Harlow Lane
Suite 312
New York, NY 10482
Website - cobaltbridgecapital.example

```html
<!DOCTYPE html>
<html lang="en">
<head>
<meta charset="utf-8">
<title>Cobalt Bridge Capital – Letterhead</title>
<link href="https://fonts.googleapis.com/css2?family=Josefin+Sans:wght@600&family=Mulish:wght@400&display=swap" rel="stylesheet">
<style>
  :root {
    --backdrop: #d9dadc;
    --paper: #f4f4f4;
    --paper-shade: #e6e6e6;
    --navy: #0c2a46;
    --slate: #5d7486;
    --ink: #3b4450;
    --white: #ffffff;
  }
  * { margin: 0; padding: 0; box-sizing: border-box; }
  html, body {
    width: 1200px; height: 780px; overflow: hidden;
    background: var(--backdrop);
  }
  .letterhead {
    position: absolute;
    left: 335px; top: 15px;
    width: 530px; height: 750px;
    background: linear-gradient(160deg, var(--paper) 0%, var(--paper-shade) 100%);
    box-shadow: 0 4px 18px rgba(0,0,0,0.18);
    overflow: hidden;
  }
  .brand {
    position: absolute; left: 38px; top: 44px;
    display: flex; align-items: center; gap: 9px;
  }
  .brand-dot {
    width: 26px; height: 26px; border-radius: 50%;
    background: var(--navy);
  }
  .brand-name {
    font-family: "Josefin Sans", sans-serif;
    font-weight: 600; font-size: 11px; line-height: 11.5px;
    letter-spacing: 0.6px; text-transform: uppercase;
    color: var(--navy);
  }
  .contact {
    position: absolute; left: 366px; top: 90px;
    display: flex; gap: 6px;
  }
  .contact-icons {
    display: flex; flex-direction: column; gap: 3px; padding-top: 1px;
  }
  .contact-icons svg { width: 7px; height: 8px; display: block; }
  .contact-rule { width: 1px; height: 32px; background: var(--navy); }
  .contact-lines {
    font-family: "Mulish", sans-serif; font-size: 7.6px; line-height: 11px;
    color: var(--ink);
  }
  .footer-wave {
    position: absolute; left: 0; bottom: 0;
    width: 530px; height: 76px; display: block;
  }
  .website {
    position: absolute; right: 30px; bottom: 16px;
    font-family: "Mulish", sans-serif; font-size: 7.6px;
    color: var(--white);
  }
</style>
</head>
<body>
  <main class="letterhead">
    <div class="brand">
      <span class="brand-dot"></span>
      <span class="brand-name">Cobalt<br>Bridge<br>Capital</span>
    </div>

    <div class="contact">
      <div class="contact-icons">
        <svg viewBox="0 0 10 10" aria-hidden="true">
          <path d="M2 1 L4 1 L4.6 3.2 L3.4 4 C4 5.4 4.8 6.2 6 6.6 L6.8 5.4 L9 6 L9 8 C9 8.6 8.6 9 8 9 C4.2 8.8 1.2 5.8 1 2 C1 1.4 1.4 1 2 1Z" fill="var(--navy)"/>
        </svg>
        <svg viewBox="0 0 10 12" aria-hidden="true">
          <path d="M5 0.5 C2.6 0.5 1 2.2 1 4.4 C1 7.2 5 11.5 5 11.5 C5 11.5 9 7.2 9 4.4 C9 2.2 7.4 0.5 5 0.5Z M5 3 A1.5 1.5 0 1 1 5 6 A1.5 1.5 0 1 1 5 3Z" fill="var(--navy)" fill-rule="evenodd"/>
        </svg>
      </div>
      <div class="contact-rule"></div>
      <div class="contact-lines">
        <p>(555) 214 - 9087</p>
        <p>58 Harlow Lane</p>
        <p>Suite 312, New York, NY 10482</p>
      </div>
    </div>

    <svg class="footer-wave" viewBox="0 0 530 76" preserveAspectRatio="none" aria-hidden="true">
      <path d="M0 26 C55 50, 150 58, 270 42 S 460 6 530 4 L530 76 L0 76 Z" fill="var(--navy)"/>
      <path d="M48 38 C150 58, 300 40, 400 18 S 500 -2 530 0" fill="none" stroke="var(--slate)" stroke-width="2.4"/>
    </svg>
    <p class="website">www.cobaltbridgecapital.example</p>
  </main>
</body>
</html>
```